MOLVT Study flyer

I need help designing a flyer for a research study that will include brain imaging in adolescents. The info is in the attached document. The study is called the Marrowby Orchard Lantern Vesper Trail (MOLVT) study. Ideally this would be returned as a document that I can edit in the future as we will have several new recruitment phases (different age groups, etc. I also would love to have a logo designed as part of this project, but I recognize that might be a separate design request.

```html
<!DOCTYPE html>
<html lang="en">
<head>
<meta charset="utf-8">
<title>MOLVT Study Flyer</title>
<link rel="stylesheet" href="https://fonts.googleapis.com/css2?family=Antonio:wght@500;600&family=DM+Sans:wght@400;600;700&display=swap">
<style>
  :root {
    --brand-purple: #a62c8a;
    --ink: #141014;
    --white: #ffffff;
    --bullet-pink: #e2509a;
    --wall-dark: #7a4a34;
    --wall-mid: #a06e52;
    --wall-light: #c99b7d;
    --linen: #e9e5e1;
    --contact-tint: #fbe9df;
  }
  * { box-sizing: border-box; margin: 0; padding: 0; }
  html, body { width: 848px; height: 1200px; overflow: hidden; background: #fff; }
  .flyer {
    width: 848px;
    height: 1200px;
    overflow: hidden;
    display: flex;
    flex-direction: column;
    font-family: "DM Sans", sans-serif;
    color: var(--white);
  }
  .masthead {
    flex: 0 0 auto;
    min-height: 295px;
    background: var(--brand-purple);
    padding: 30px 52px 26px 52px;
    font-family: "Antonio", sans-serif;
  }
  .masthead__question {
    color: var(--ink);
    font-weight: 500;
    font-size: 24px;
    line-height: 1;
    white-space: nowrap;
  }
  .masthead__headline {
    margin-top: 22px;
    color: var(--white);
    font-weight: 600;
    font-size: 44px;
    line-height: 48px;
    text-transform: uppercase;
    letter-spacing: 0.4px;
  }
  .content {
    position: relative;
    flex: 1 1 auto;
  }
  .content__photo {
    position: absolute; inset: 0;
    background:
      linear-gradient(180deg, rgba(233,229,225,0) 72%, var(--linen) 90%),
      linear-gradient(100deg, var(--wall-dark) 0%, var(--wall-mid) 50%, var(--wall-light) 100%);
  }
  .details {
    position: absolute; left: 52px; top: 35px;
    font-size: 15.5px; line-height: 19px;
  }
  .details__title { font-weight: 700; font-size: 15.8px; line-height: 21px; }
  .details__list { list-style: none; margin-top: 4px; }
  .details__list li { position: relative; padding-left: 12px; }
  .details__list li + li { margin-top: 2px; }
  .details__list li::before {
    content: ""; position: absolute; left: 1px; top: 7px;
    width: 4px; height: 4px; border-radius: 50%; background: var(--bullet-pink);
  }
  .details__block--involves { width: 250px; }
  .details__block--eligibility { margin-top: 24px; width: 220px; }
  .details__block--eligibility .details__title { width: 165px; }
  .details__list--eligibility li { padding-left: 16px; }
  .contact {
    position: absolute; right: 51px; top: 35px;
    text-align: right;
  }
  .contact__call {
    font-weight: 700; font-size: 15.3px; line-height: 20.5px; letter-spacing: 0.2px;
    text-transform: uppercase; color: var(--contact-tint);
  }
  .contact__email {
    margin-top: 7px; color: var(--ink); font-weight: 600; font-size: 15.3px; letter-spacing: 0.4px;
  }
  .payment {
    position: absolute; left: 667px; top: 132px;
    width: 130px; height: 130px; border-radius: 50%;
    background: var(--brand-purple);
    font-family: "Antonio", sans-serif;
    text-align: center;
  }
  .payment__label { margin-top: 30px; font-size: 13px; font-weight: 500; }
  .payment__amount { font-size: 50px; font-weight: 600; line-height: 52px; }
  .identity {
    position: absolute; left: 621px; top: 590px;
    display: flex; align-items: flex-start; gap: 10px;
  }
  .identity__mark { width: 44px; height: 44px; border-radius: 50%; background: var(--white); margin-top: 2px; }
  .identity__name { font-weight: 700; font-size: 27px; line-height: 28px; letter-spacing: 1px; }
  .identity__tagline { margin-top: 6px; font-size: 11px; line-height: 12.5px; width: 160px; }
</style>
</head>
<body>
<main class="flyer">
  <header class="masthead">
    <p class="masthead__question">Are you the parent of a child age 10–17? Do they worry or overthink negative emotions?</p>
    <h1 class="masthead__headline">Harrowgate University researchers are seeking girls age 10–17 for a study about brain activity in emotions and decision-making and how they relate to puberty, anxiety and depression.</h1>
  </header>

  <div class="content">
    <div class="content__photo" role="img" aria-label="Photo of a teenage girl sitting cross-legged on a bed hugging a pillow, her head hidden by a white cloud, against a warm brown wall"></div>

    <section class="details">
      <div class="details__block details__block--involves">
        <h2 class="details__title">Study participation involves:</h2>
        <ul class="details__list">
          <li>One one-hour interview (online or in-person) where your child will discuss their thoughts</li>
          <li>Online questionnaires (parent and child)</li>
          <li>One two-hour visit where your child will complete an MRI scan, answer questions about their puberty stage, and have a small hair sample taken to study puberty hormones</li>
        </ul>
      </div>
      <div class="details__block details__block--eligibility">
        <h2 class="details__title">Your child may be eligible if they:</h2>
        <ul class="details__list details__list--eligibility">
          <li>Are age 10–17</li>
          <li>Tend to worry or overthink negative thoughts</li>
          <li>have not been diagnosed with psychosis, learning problems, or autism</li>
        </ul>
      </div>
    </section>

    <section class="contact">
      <p class="contact__call">Interested in participating?<br>Want more information?<br>Please contact us!</p>
      <p class="contact__email">molvtstudy@harrowgate.edu</p>
    </section>

    <div class="payment">
      <p class="payment__label">Compensation up to</p>
      <p class="payment__amount">$140</p>
    </div>

    <div class="identity">
      <span class="identity__mark"></span>
      <div>
        <p class="identity__name">MOLVT</p>
        <p class="identity__tagline">Marrowby Orchard Lantern Vesper Trail</p>
      </div>
    </div>
  </div>
</main>
</body>
</html>
```